www.brevatin.com Sales/Order Page ReDesign

We need a new and amazing design for our sales/order page to attract more costumers and new houses for our portal.

Here is the existing page with the current design: https://www.brevatin.com/sales

We are proud owners of www.sommarhytta.no and www.brevatin.com and we want more holiday home owners to join our page so that we can rent out their holiday homes and increase the number of houses on our portal.

To get more homeowners we need a sales page that can sell our products the best way possible. Therefore we want you too blow us away with a fresh, modern, easy understandable and stylish new sales/order page.

The only restrictions we give when it comes to design is that it needs to fit the existing design of our portals, the top and footer are set. Beside that we are open for everything as long as it at once give the customers impression that this is a good, professional page were they just have to put out their houses.

When it comes to content I have added two documents who include the content to put in here and some guidelines on how to organize the page. Please be creative and add necessary graphics, symbols, background pictures and what ever necessary to make this page look professional and appealing to new costumers.

Looking forward to what suggestions we are given.

We just want to inform that we have updated our brief with a much more concrete description of what content to add on the sale page, and who to structure the content on the page. Hope this helps to make suggestions easier. Looking forward to receive some good contributions.

We would just like to make sure that everyone have understood that we are not asking for a new design suggestion to our portal in general. We are only asking for a redesign of our sales/order page you find here www.brevatin.com/sales. We have to day received some designs for our front page and the design it self was good, but that's not what we are asking for this time and don't want you to use time of something we don't need at the moment. We are looking forward too se some good suggestions.

Reason: Hello. Thanks for all the great contributions we have been given so fare. We haven't been able to respond to all design and are therefore extending the deadline so that we are able to respond to the designs we have been giver and to gov time to make final changes.

Reason: We are extending the deadline to give designers time to give new suggestion based on our latest feedback today.

Reason: Extended so we can receive last design changes.

Target Market(s)

This is a presentation page where we present our product agains new home owner who we what to choose listing there property on or site.

Industry/Entity Type

Sales

Requirements
Must have
• A modern design who calms the costumer down and help them in deciding to chose us, and for them to choose us they need to trust and believe in us. Therefore your main task is to create a page that effectively informs about our product, gets the visitors attentions and make them trust us.
Nice to have
• Examples of good competitors and good order pages we like:

http://www.cabinquest.example/info/lyp?icid=IL___O_Text___top_nav_link
https://www.nestlodge.example/rooms/new
https://www.pearvix.example/phone/compare/
http://www.guestnook.example/host
Should not have
• - Bad design :-). With bad design we mean design that looks like it's made in 2 seconds by a little child.

```html
<!DOCTYPE html>
<html lang="en">
<head>
<meta charset="utf-8">
<title>Brevatin – List your property</title>
<link href="https://fonts.googleapis.com/css2?family=Roboto:wght@300;400;500;700&family=Cinzel:wght@900&family=Handlee&display=swap" rel="stylesheet">
<style>
:root{
  --blue:#1a8ad6;
  --blue-dark:#0f6fb4;
  --ink:#222;
  --muted:#555;
  --page:#f3f3f3;
  --green:#8dc63f;
  --green-dark:#6fa52a;
  --white:#fff;
}
*{box-sizing:border-box;margin:0;padding:0}
html,body{width:983px;height:1200px;overflow:hidden}
body{position:relative;background:var(--page);font-family:'Roboto',sans-serif;color:var(--ink)}
.top-bar{position:absolute;left:0;top:0;width:983px;height:46px;background:var(--blue);z-index:3}
.hero{position:absolute;left:0;top:46px;width:983px;height:442px;
  background:linear-gradient(180deg,#3d9be0 0%,#9fd1ee 14%,#6ea98c 24%,#2fb5c4 33%,#5fd2d6 45%,#a9e6e5 56%,#e8f6f6 66%,#ffffff 76%)}
.hero-white{position:absolute;left:0;top:380px;width:983px;height:108px;background:#fff}
.brand-panel{position:absolute;left:106px;top:0;width:279px;z-index:4}
.brand-name{position:absolute;left:0;top:42px;width:279px;text-align:center;font:500 40px 'Roboto',sans-serif;color:var(--blue)}
.lang{position:absolute;top:13px;width:27px;height:19px;z-index:4}
.sign-in{position:absolute;left:633px;top:7px;width:132px;height:33px;background:var(--green);border:1px solid var(--green-dark);border-radius:3px;z-index:4;color:#24400a;font:500 13px 'Roboto',sans-serif;display:flex;align-items:center;padding-left:33px}
.sign-in::after{content:"";position:absolute;right:13px;top:14px;border:4px solid transparent;border-top-color:#2a4a0c}
.list-link{position:absolute;left:774px;top:13px;z-index:4;color:var(--white);font:700 15px 'Roboto',sans-serif}
.hero-title{position:absolute;left:0;top:262px;width:983px;text-align:center;font:900 47px 'Cinzel',serif;color:#f6f6f6;letter-spacing:1px;text-shadow:0 2px 0 #999,0 3px 5px rgba(0,0,0,.45);z-index:2}
.hero-sub{position:absolute;left:0;top:318px;width:983px;text-align:center;font:400 27px 'Roboto',sans-serif;color:#111;z-index:2}
.script{position:absolute;left:246px;top:392px;width:170px;text-align:center;font:400 25px/28px 'Handlee',cursive;color:#222}
.pitch{position:absolute;left:487px;top:388px;z-index:2}
.pitch h3{font:300 20px 'Roboto',sans-serif;color:#333}
.pitch p{font:300 16px/20px 'Roboto',sans-serif;color:#444;margin-top:4px}
.pitch em{font-weight:700;font-style:italic}
.band{position:absolute;left:0;top:487px;width:983px;height:48px;background:var(--blue);color:var(--white);text-align:center;font:300 22px/48px 'Roboto',sans-serif}
.multi{position:absolute;left:677px;top:548px;display:flex;align-items:center;gap:8px;color:var(--blue);font:400 14px 'Roboto',sans-serif}
.feature{position:absolute;width:320px}
.feature h4{font:400 19px 'Roboto',sans-serif;color:#111;margin-bottom:3px}
.feature p{font:300 12.5px/15px 'Roboto',sans-serif;color:#444}
.icon{position:absolute;width:46px;height:46px}
.icon svg{width:46px;height:46px;fill:none;stroke:var(--blue);stroke-width:2;stroke-linejoin:round;stroke-linecap:round}
</style>
</head>
<body>
<div class="top-bar"></div>
<div class="hero" role="img" aria-label="Photo of a tropical beach with turquoise water, palm trees and a thatched hut, fading to white"></div>
<div class="hero-white"></div>

<svg class="brand-panel" width="279" height="135" viewBox="0 0 279 135" aria-hidden="true">
  <path d="M0 0H279V105L139.5 135 0 105Z" fill="#f4f4f4"/>
  <path d="M0 88L139.5 118 279 88V105L139.5 135 0 105Z" fill="#3a3a3a"/>
</svg>
<div class="brand-name" style="left:106px;z-index:5">Brevatin</div>

<svg class="lang" style="left:560px" viewBox="0 0 27 19" aria-label="Norwegian">
  <rect width="27" height="19" fill="#c8102e"/><rect x="7" width="5" height="19" fill="#fff"/><rect y="7" width="27" height="5" fill="#fff"/>
  <rect x="8.5" width="2" height="19" fill="#00205b"/><rect y="8.5" width="27" height="2" fill="#00205b"/>
</svg>
<svg class="lang" style="left:592px" viewBox="0 0 27 19" aria-label="English">
  <rect width="27" height="19" fill="#012169"/><path d="M0 0L27 19M27 0L0 19" stroke="#fff" stroke-width="4"/>
  <path d="M0 0L27 19M27 0L0 19" stroke="#c8102e" stroke-width="1.5"/>
  <rect x="11" width="5" height="19" fill="#fff"/><rect y="7" width="27" height="5" fill="#fff"/>
  <rect x="12" width="3" height="19" fill="#c8102e"/><rect y="8" width="27" height="3" fill="#c8102e"/>
</svg>
<div class="sign-in"><svg style="position:absolute;left:13px;top:10px" width="10" height="12" viewBox="0 0 10 12"><rect x="1" y="5" width="8" height="7" fill="#2a4a0c"/><path d="M3 5V3a2 2 0 0 1 4 0v2" stroke="#2a4a0c" fill="none" stroke-width="1.5"/></svg>Sign in</div>
<div class="list-link">List your property</div>

<h1 class="hero-title">LIST YOUR PROPERTY TODAY!</h1>
<p class="hero-sub">Brevatin helps you make money on your property, starting now...</p>

<div class="script">On Brevatin<br>you can rent out</div>
<svg style="position:absolute;left:350px;top:425px" width="130" height="40" viewBox="0 0 130 40" aria-hidden="true">
  <path d="M5 28Q60 42 118 20" stroke="#999" stroke-width="2" fill="none"/>
  <path d="M108 14L120 19 111 29" stroke="#999" stroke-width="2" fill="none"/>
</svg>
<div class="pitch">
  <h3>And make a profit on it. You ask how?</h3>
  <p>Keep reading and we will let you know<br>how <em>easy</em> and <em>hassle free</em> it is!</p>
</div>

<div class="band">All our announcements have the following services included</div>

<div class="multi">
  <svg width="36" height="16" viewBox="0 0 36 16" fill="#888"><path d="M1 10L7 5 13 10V16H1Z"/><path d="M11 8L18 1 25 8V16H11Z" fill="#777"/><path d="M23 10L29 5 35 10V16H23Z"/></svg>
  Advertising 5+ properties?
</div>

<!-- Left column -->
<div class="icon" style="left:121px;top:600px"><svg viewBox="0 0 46 46"><circle cx="23" cy="11" r="8"/><path d="M9 42V31q0-8 14-8t14 8v11Z"/><path d="M20 23l3 12 3-12"/></svg></div>
<div class="feature" style="left:187px;top:593px"><h4>Help from professionals</h4><p>Let professionals who know the travel industries handle all yours booking requests. Great result with less work, our professional team will answer all you inquiries.</p></div>

<div class="icon" style="left:121px;top:697px"><svg viewBox="0 0 46 46"><path d="M6 16H40L38 42H8Z"/><path d="M16 20V11a7 7 0 0 1 14 0v9"/></svg></div>
<div class="feature" style="left:187px;top:688px"><h4>Access Scandinavians</h4><p>Our roots are from Norway, and we have expertise with the Scandinavian market and can help you get tenants from these very travel friendly demographics.</p></div>

<div class="icon" style="left:118px;top:797px"><svg viewBox="0 0 46 46"><circle cx="23" cy="23" r="20"/><circle cx="23" cy="23" r="14"/><rect x="6" y="17" width="34" height="12" rx="2" fill="#fff"/><path d="M11 20v7M11 20h4M11 23h3M18 20h3M18 20v7h3M18 23h2M25 20h3M25 20v7h3M25 23h2M35 20h-3v3.5h3V27h-3"/></svg></div>
<div class="feature" style="left:188px;top:787px"><h4>No Traveler fees</h4><p>Unlike many other vacation rental booking sites, travelers can book vacation rentals without paying any fees to us, maybe one of the reason we have so many returning costumers.</p></div>

<div class="icon" style="left:121px;top:893px"><svg viewBox="0 0 46 46"><rect x="3" y="24" width="40" height="18"/><circle cx="23" cy="14" r="11"/><path d="M26 10h-4a2 2 0 0 0 0 4h2a2 2 0 0 1 0 4h-4M23 7v3M23 18v3M10 33h26"/></svg></div>
<div class="feature" style="left:187px;top:883px"><h4>Payments by Brevatin</h4><p>Guests are always carful when it comes to payment. Everybody can feel safe through secure payment with Brevatin. We are responsible for you getting paid.</p></div>

<div class="icon" style="left:121px;top:984px"><svg viewBox="0 0 46 46"><path d="M6 40L22 24M26 20L40 6l-4 0-2 2 0 4-4 0"/><path d="M8 8a8 8 0 0 0 10 10l20 20a3 3 0 0 1-4 4L14 22A8 8 0 0 1 4 12l5 3 3-3Z"/></svg></div>
<div class="feature" style="left:185px;top:977px"><h4>Easy-to-Use Tools</h4><p>Get access too a very well developed reservation and management tool that helps you keep track of bookings.</p></div>

<div class="icon" style="left:121px;top:1078px"><svg viewBox="0 0 46 46"><rect x="5" y="8" width="36" height="34" rx="3"/><path d="M5 17H41M14 4v8M32 4v8"/><text x="23" y="36" text-anchor="middle" font-family="Roboto" font-size="14" font-weight="700" fill="#1a8ad6" stroke="none">27</text></svg></div>
<div class="feature" style="left:185px;top:1068px"><h4>Online calendar</h4><p>Tenants like to know when your property is available straight away, and we let them know that. At the same time you can easily manage your availability.</p></div>

<!-- Right column -->
<div class="icon" style="left:510px;top:600px"><svg viewBox="0 0 46 46"><path d="M4 16H42V42H4Z"/><path d="M15 16V10a8 8 0 0 1 16 0v6"/><path d="M15 32l8-7 8 7M18 30v7h10v-7"/></svg></div>
<div class="feature" style="left:575px;top:590px"><h4>Broad exposure</h4><p>We have been in the market for several years and are promoting your property through the necessary and right channels.</p></div>

<div class="icon" style="left:508px;top:697px"><svg viewBox="0 0 46 46"><circle cx="23" cy="23" r="20"/><path d="M9 14h28M9 32h28"/><rect x="5" y="17" width="36" height="12" rx="2" fill="#1a8ad6"/><text x="23" y="27" text-anchor="middle" font-family="Roboto" font-size="9" font-weight="700" fill="#fff" stroke="none">SAFE</text></svg></div>
<div class="feature" style="left:575px;top:688px"><h4>Trust &amp; Safety</h4><p>You are still in control of your property. We have the tools to help you accept a booking only if you're 100% comfortable.</p></div>

<div class="icon" style="left:513px;top:795px"><svg viewBox="0 0 46 46"><rect x="4" y="4" width="38" height="38"/><rect x="9" y="9" width="28" height="28"/><path d="M17 15l14 14M24 24l-5 7M24 24l9-4M20 20l4-7"/></svg></div>
<div class="feature" style="left:575px;top:786px"><h4>Online Booking</h4><p>We simplify the booking process by allowing tenants to send online reservations request, which gives you a 24-hour period to accept or decline their reservation.</p></div>

<div class="icon" style="left:513px;top:893px"><svg viewBox="0 0 46 46"><rect x="4" y="3" width="38" height="40"/><rect x="9" y="8" width="28" height="30"/><text x="23" y="30" text-anchor="middle" font-family="Roboto" font-size="17" fill="#1a8ad6" stroke="none">?</text></svg></div>
<div class="feature" style="left:575px;top:883px"><h4>Unlimited inquiries</h4><p>When you are renting out your property you need inquiries, therefore we have no fees on inquiries for your property.</p></div>

<div class="icon" style="left:513px;top:990px"><svg viewBox="0 0 46 46"><path d="M4 12H24l3-4H42V40H4Z"/><circle cx="23" cy="26" r="5"/><path d="M23 17v3M23 32v3M14 26h3M29 26h3M17 20l2 2M27 30l2 2M17 32l2-2M27 22l2-2"/></svg></div>
<div class="feature" style="left:575px;top:982px"><h4>Unlimited photos</h4><p>A picture says more then 1000 words, therefore we inspire you too upload as many pictures as possible.</p></div>

<div class="icon" style="left:509px;top:1078px"><svg viewBox="0 0 46 46"><path d="M23 32C14 21 14 17 14 13a9 9 0 0 1 18 0c0 4 0 8-9 19Z"/><circle cx="23" cy="13" r="3"/><path d="M3 42l7-10h7M29 32h7l7 10M3 42h40"/></svg></div>
<div class="feature" style="left:575px;top:1068px"><h4>Map and location</h4><p>Tenants are always wondering where your property is located. Show them through our map and let them know where nearby attractions are.</p></div>
</body>
</html>
```